TRESSLY FACEBOOK DESIGN

I need new design for facebook https://www.facebook.com/tresslyitalia.
Our Businnes is Hair care , hair replacement , hair transplant . hair regrowth . i NEED MEDICAL AND PROFESSIONAL DESIGN. I NEED ALSO RESPONSIVE DESIGN

Target Market(s)

Consumers

Industry/Entity Type

MEDICAL AND COSMETICS

Colors
0054AA
0677BA
7BADD7
CADEEF
E8F1F8

Requirements
Must have
• MEDICAL
Nice to have
• RESPONSIVE DESIGN

```html
<!DOCTYPE html>
<html lang="it">
<head>
<meta charset="utf-8">
<title>Tressly – Facebook Cover</title>
<link rel="stylesheet" href="https://fonts.googleapis.com/css2?family=Maven+Pro:wght@500;700&family=Quicksand:wght@500;700&display=swap">
<style>
  :root {
    --navy: #004C97;
    --brand-blue: #0054AA;
    --sky: #2CABE2;
    --ink: #1d1d1f;
    --white: #ffffff;
    --page-bg: #eceef1;
    --rule: #9aa3ad;
  }
  * { margin: 0; padding: 0; box-sizing: border-box; }
  html, body {
    width: 959px; height: 1200px; overflow: hidden;
    background: var(--page-bg);
  }
  .cover {
    position: absolute; left: 30px; top: 433px;
    width: 900px; height: 333px;
    background: var(--white);
    box-shadow: 0 4px 10px rgba(0,0,0,.18);
    overflow: hidden;
    font-family: "Quicksand", sans-serif;
  }
  .cover-waves { position: absolute; inset: 0; width: 100%; height: 100%; }

  .brand { position: absolute; left: 126px; top: 74px; width: 240px; }
  .brand-name {
    display: flex; align-items: center; gap: 10px;
    font-family: "Maven Pro", sans-serif; font-weight: 700;
    font-size: 48px; line-height: 1; color: var(--navy); letter-spacing: -0.5px;
  }
  .brand-dot { width: 36px; height: 36px; border-radius: 50%; background: var(--sky); flex: none; }
  .brand-tagline {
    margin-top: 8px; font-family: "Maven Pro", sans-serif; font-weight: 500;
    font-size: 12.6px; color: var(--brand-blue); letter-spacing: .2px; white-space: nowrap;
  }

  .divider { position: absolute; left: 449px; top: 78px; width: 1px; height: 100px; background: var(--rule); }

  .pill {
    position: absolute; display: flex; align-items: center; justify-content: center;
    background: var(--sky); color: var(--white);
    font-family: "Maven Pro", sans-serif; font-weight: 500;
    border-radius: 20px; white-space: nowrap;
  }
  .services-pill { left: 591px; top: 66px; width: 161px; height: 33px; font-size: 20px; }
  .services-list {
    position: absolute; left: 520px; top: 106px; width: 303px; text-align: center;
    font-size: 21px; font-weight: 500; color: var(--ink); line-height: 26px; white-space: nowrap;
  }
  .services-list .sep { color: var(--sky); font-size: 14px; vertical-align: 3px; padding: 0 4px; }
  .visit-pill { left: 624px; top: 175px; width: 96px; height: 29px; font-size: 20px; }
  .web-address {
    position: absolute; left: 520px; top: 204px; width: 303px; text-align: center;
    font-family: "Maven Pro", sans-serif; font-weight: 700; font-size: 31px; color: var(--navy);
  }
  .web-address .domain { color: var(--sky); }

  .call-pill { left: 128px; top: 243px; width: 92px; height: 29px; font-size: 21px; }
  .phone {
    position: absolute; left: 127px; top: 278px;
    font-family: "Maven Pro", sans-serif; font-weight: 700; font-size: 32px;
    color: var(--white); letter-spacing: .3px;
  }
</style>
</head>
<body>
  <section class="cover" aria-label="Tressly cover">
    <svg class="cover-waves" viewBox="0 0 1302 482" preserveAspectRatio="none" aria-hidden="true">
      <path fill="var(--sky)" d="M0,285 C180,270 340,288 470,332 C330,306 160,306 0,322 Z"/>
      <path fill="var(--navy)" d="M0,340 C260,300 560,340 850,400 C1020,432 1170,418 1302,356 L1302,482 L0,482 Z"/>
      <path fill="var(--sky)" d="M1302,288 C1200,368 1050,404 850,410 C1050,418 1210,398 1302,340 Z"/>
    </svg>

    <div class="brand">
      <div class="brand-name"><span class="brand-dot"></span>Tressly</div>
      <div class="brand-tagline">CURA E REINTEGRAZIONE DEI CAPELLI</div>
    </div>

    <div class="divider"></div>

    <div class="pill services-pill">Our Services:</div>
    <p class="services-list">
      Hair care<span class="sep">●</span>hair replacement<br>
      hair transplant<span class="sep">●</span>hair regrowth
    </p>
    <div class="pill visit-pill">Visit Us</div>
    <p class="web-address">www.<span class="domain">tressly</span>.it</p>

    <div class="pill call-pill">Call Us</div>
    <p class="phone">800-412-386</p>
  </section>
</body>
</html>
```